PRICE LIST

I wont a design similar to my business card but not black i wont it very easy to read and simple here is my price list so far

Industry/Entity Type

Business

Font styles to use
Script

```html
<!DOCTYPE html>
<html lang="en">
<head>
<meta charset="utf-8">
<title>Petal Beauty – Price List</title>
<link href="https://fonts.googleapis.com/css2?family=Pinyon+Script&family=Cormorant+Garamond:ital,wght@1,500&family=Open+Sans:wght@300;400;600&display=swap" rel="stylesheet">
<style>
  :root {
    --page-bg: #ededed;
    --panel-top: #e4e4e6;
    --panel-mid: #ffffff;
    --ink: #2e2e2e;
    --ink-soft: #555555;
    --ink-muted: #7a7a7a;
    --rose: #c29a86;
    --rose-light: #d9b9a8;
    --hair: #4a3226;
    --skin: #e8c8b4;
    --skin-light: #f3e2d6;
  }
  * { margin: 0; padding: 0; box-sizing: border-box; }
  html, body { width: 1200px; height: 1000px; overflow: hidden; background: var(--page-bg); }
  .price-list {
    position: absolute; left: 58px; top: 120px; width: 1086px; height: 760px;
    background: linear-gradient(180deg, var(--panel-top) 0%, var(--panel-mid) 30%, var(--panel-mid) 75%, var(--panel-top) 100%);
    overflow: hidden;
    font-family: "Open Sans", Arial, sans-serif;
    color: var(--ink);
  }
  .portrait {
    position: absolute; left: 0; top: 0; width: 500px; height: 760px;
    background:
      radial-gradient(ellipse 260px 200px at 170px 90px, var(--hair) 0%, rgba(74,50,38,0.7) 55%, rgba(74,50,38,0) 100%),
      radial-gradient(ellipse 300px 420px at 230px 420px, var(--skin) 0%, var(--skin-light) 60%, rgba(243,226,214,0) 100%),
      linear-gradient(180deg, #d8b5a0 0%, var(--skin-light) 100%);
    -webkit-mask-image: linear-gradient(90deg, #000 65%, transparent 100%);
    mask-image: linear-gradient(90deg, #000 65%, transparent 100%);
  }
  .brand-title {
    position: absolute; left: 522px; top: 40px; font-weight: 400;
    font-family: "Pinyon Script", cursive; font-size: 84px; line-height: 1; color: var(--ink);
  }
  .brand-sub {
    position: absolute; left: 666px; top: 133px;
    font-size: 16px; font-weight: 600; letter-spacing: 1.5px; color: var(--ink-soft);
  }
  .tagline {
    position: absolute; left: 504px; top: 168px;
    font-size: 27px; font-weight: 600; letter-spacing: 2px; color: var(--rose); white-space: nowrap;
  }
  .section-title {
    position: absolute; top: 250px; font-weight: 400;
    font-family: "Pinyon Script", cursive; font-size: 27px; color: var(--ink); white-space: nowrap;
  }
  .section-title.nails { left: 434px; }
  .section-title.wax { left: 797px; }
  .service { position: absolute; }
  .service-name { font-size: 18px; font-weight: 300; color: var(--ink); white-space: nowrap; }
  .service-note { font-size: 11.5px; letter-spacing: 0.8px; color: var(--ink-muted); line-height: 16px; text-transform: uppercase; white-space: nowrap; }
  .price {
    position: absolute; font-family: "Cormorant Garamond", serif; font-style: italic; font-weight: 500;
    font-size: 36px; line-height: 1; color: var(--rose);
  }
  .tan-offer {
    position: absolute; left: 413px; top: 558px; font-size: 17px; font-weight: 300; color: var(--ink); white-space: nowrap;
  }
  .partner {
    position: absolute; top: 664px; display: flex; align-items: center; gap: 8px;
    font-size: 24px; font-weight: 600; color: var(--ink);
  }
  .partner-mark { width: 14px; height: 14px; background: var(--ink); }
  .partner-divider { position: absolute; left: 273px; top: 645px; width: 1px; height: 100px; background: #b8b8b8; }
  .social { position: absolute; top: 660px; display: flex; align-items: center; gap: 12px; }
  .social-mark { width: 42px; height: 42px; background: var(--rose-light); }
  .social-mark.round { border-radius: 50%; }
  .social-label { font-size: 15px; font-weight: 600; letter-spacing: 1px; color: var(--rose); line-height: 17px; }
  .social-handle { font-size: 12px; font-weight: 600; letter-spacing: 1px; color: var(--ink-soft); }
  .rule { position: absolute; left: 510px; width: 576px; height: 1px; background: var(--rose-light); }
  .contact {
    position: absolute; top: 731px; font-size: 12px; font-weight: 400; letter-spacing: 1px; color: var(--ink-muted);
    white-space: nowrap;
  }
</style>
</head>
<body>
<main class="price-list">
  <div class="portrait" role="img" aria-label="Portrait photograph of a woman with short dark hair resting her chin on her shoulder"></div>

  <h1 class="brand-title">Petal Beauty</h1>
  <div class="brand-sub">FROM HOME</div>
  <h2 class="tagline">QUALIFIED BEAUTY THERAPIST</h2>

  <h3 class="section-title nails">Manicures &amp; Pedicures</h3>
  <h3 class="section-title wax">Waxing and Tinting</h3>

  <div class="service" style="left:426px;top:317px">
    <div class="service-name">Shellac Manicure/Pedicure</div>
    <div class="service-note">Cut, shape, cuticles and shellac</div>
  </div>
  <span class="price" style="left:680px;top:309px">30</span>

  <div class="service" style="left:426px;top:375px">
    <div class="service-name">Deluxe Manicure/Pedicure</div>
    <div class="service-note">Soak, exfoliate, cut, shape, cuticles<br>and polish or + shellac for $10</div>
  </div>
  <span class="price" style="left:678px;top:367px">40</span>

  <div class="service" style="left:426px;top:450px">
    <div class="service-name">Paraffin Manicure/Pedicure</div>
    <div class="service-note">Soak, exfoliate, parrafin treatmen,<br>cut, shape, cuticles<br>and polish or + shellac for $5</div>
  </div>
  <span class="price" style="left:680px;top:442px">45</span>

  <div class="service" style="left:810px;top:317px"><div class="service-name">Eyebrow Wax</div></div>
  <span class="price" style="left:955px;top:309px">10</span>
  <div class="service" style="left:810px;top:356px"><div class="service-name">Eyebrow Tint</div></div>
  <span class="price" style="left:955px;top:348px">10</span>
  <div class="service" style="left:810px;top:395px"><div class="service-name">Eyelash Tint</div></div>
  <span class="price" style="left:955px;top:387px">10</span>
  <div class="service" style="left:810px;top:434px"><div class="service-name">Lip Wax</div></div>
  <span class="price" style="left:955px;top:426px">10</span>
  <div class="service" style="left:810px;top:473px"><div class="service-name">Chin Wax</div></div>
  <span class="price" style="left:955px;top:465px">10</span>
  <div class="service" style="left:810px;top:512px"><div class="service-name">Underarm</div></div>
  <span class="price" style="left:955px;top:504px">15</span>

  <p class="tan-offer">The very popular “2 Hour SUNVEIL TAN“in all ranges is now available</p>
  <span class="price" style="left:966px;top:550px">25</span>

  <div class="partner" style="left:112px"><span>Lumen</span><span class="partner-mark"></span></div>
  <div class="partner-divider"></div>
  <div class="partner" style="left:298px"><span class="partner-mark" style="border-radius:50%"></span><span>SunVeil</span></div>

  <div class="social" style="left:528px">
    <span class="social-mark round"></span>
    <div><div class="social-label">OUR PAGE</div><div class="social-handle">PETAL BEAUTY CORAL BAY</div></div>
  </div>
  <div class="social" style="left:796px">
    <span class="social-mark"></span>
    <div><div class="social-label">PHOTO FEED</div><div class="social-handle">PETALBEAUTYCORALBAY</div></div>
  </div>

  <div class="rule" style="top:710px"></div>
  <div class="rule" style="top:715px"></div>

  <div class="contact" style="left:297px">MAREN &nbsp;|&nbsp; PH: 0412 000 318</div>
  <div class="contact" style="left:527px">LOCATED IN SEABROOK, CORAL BAY</div>
  <div class="contact" style="right:14px">FLEXIBLE HOURS 7 DAYS A WEEK</div>
</main>
</body>
</html>
```